Label for packages of Pure Raw Natural Honeycomb

This is a label that will be used to sell pure raw honeycomb on the internet and in farm gate sales
Label must contain my Logo (which is attached)
my website www.meadowglintfarm.ca
the weight 300 gr and the words Pure Raw Honeycomb
label design should fit onto a sticker 3" by 2" oval but If the size appears to small to get all that info on I am willing to look at a different size or shape

Target Market(s)

internet and in person farm gate customers

Industry/Entity Type

Agriculture

Font styles to use
Other font styles liked:
• the font should compliment my logo font

Colors
ffc214

Requirements
Must have
• Label must contain my Logo (attached) my website www.meadowglintfarm.ca
• the weight 300 gr and the words Pure Raw Honeycomb would like something in black and gold with a bit of an Elegant vintage feel
Nice to have
• vintage feel
• If the size appears to small to get all that info on I am willing to look at a different size or shape
Should not have
• no cartoons

```html
<!DOCTYPE html>
<html lang="en">
<head>
<meta charset="utf-8">
<title>Meadowglint Farm – Pure Raw Honeycomb Label</title>
<link rel="stylesheet" href="https://fonts.googleapis.com/css2?family=Lobster&family=Open+Sans:wght@400&display=swap">
<style>
  :root {
    --paper: #ffffff;
    --label-black: #000000;
    --rim-grey: #1a1a1a;
    --honey-gold: #ffc214;
    --honey-gold-deep: #f5ab0c;
  }
  * { margin: 0; padding: 0; box-sizing: border-box; }
  html, body {
    width: 1200px;
    height: 900px;
    overflow: hidden;
    background: var(--paper);
  }
  .canvas {
    position: relative;
    width: 1200px;
    height: 900px;
    background: var(--paper);
  }
  .label-shape {
    position: absolute;
    inset: 0;
  }
  .brand-name {
    position: absolute;
    left: 0;
    width: 1200px;
    top: 340px;
    text-align: center;
    font-family: "Lobster", cursive;
    font-size: 64px;
    line-height: 1;
    color: var(--honey-gold);
  }
  .product-title {
    position: absolute;
    left: 0;
    width: 1200px;
    top: 522px;
    text-align: center;
    font-family: "Lobster", cursive;
    font-size: 44px;
    line-height: 1;
    color: var(--honey-gold);
  }
  .website {
    position: absolute;
    left: 0;
    width: 1200px;
    top: 636px;
    text-align: center;
    font-family: "Open Sans", sans-serif;
    font-size: 21px;
    color: var(--honey-gold-deep);
  }
  .net-weight {
    position: absolute;
    left: 0;
    width: 1200px;
    top: 684px;
    text-align: center;
    font-family: "Open Sans", sans-serif;
    font-size: 17px;
    color: var(--honey-gold-deep);
  }
</style>
</head>
<body>
<main class="canvas">
  <svg class="label-shape" width="1200" height="900" viewBox="0 0 1200 900" aria-hidden="false">
    <!-- oval sticker body -->
    <ellipse class="label-body" cx="600" cy="447" rx="452" ry="305" fill="var(--label-black)" stroke="var(--rim-grey)" stroke-width="3"/>
    <ellipse class="label-inner-ring" cx="600" cy="447" rx="430" ry="284" fill="none" stroke="var(--honey-gold)" stroke-width="3"/>

    <!-- title band rules -->
    <g class="title-band" stroke="var(--honey-gold)">
      <line x1="273" y1="507" x2="927" y2="507" stroke-width="3"/>
      <line x1="273" y1="515" x2="927" y2="515" stroke-width="1.5"/>
      <line x1="273" y1="578" x2="927" y2="578" stroke-width="1.5"/>
      <line x1="273" y1="586" x2="927" y2="586" stroke-width="3"/>
    </g>

    <!-- vintage flourish placeholders -->
    <rect class="flourish flourish-top" x="566" y="486" width="68" height="20" rx="4" fill="var(--honey-gold)" role="img" aria-label="Gold vintage filigree flourish above the title band"/>
    <rect class="flourish flourish-bottom" x="566" y="588" width="68" height="22" rx="4" fill="var(--honey-gold)" role="img" aria-label="Gold vintage filigree flourish below the title band"/>
  </svg>

  <div class="brand-name">Meadowglint Farm</div>
  <h1 class="product-title">Pure Raw Honeycomb</h1>
  <p class="website">www.meadowglintfarm.ca</p>
  <p class="net-weight">weight 300 gr</p>
</main>
</body>
</html>
```